Custom Framing Shop Stonebrook Framing Studio

I want an eye catching graphic that will be used a s business sign on a busy road. The sign MUST communicate the type of business it is clearly to vehicles traveling at 40 mph. This is a custom picture framing business and the sign will be hanging and be approximately 32" X 48". The business name is Stonebrook Framing Studio; Custom framing: by appointment and should include a whole or partial image of a picture frame as a visual que. I've included inspiration idea's, color pallets and styles that I like and a current business card for inspiration. I like the crimson font style shadowing and background colors of the attached Pello's pizzeria sign. I'd prefer crimson letters. Custom Framing is the message to communicate, followed by phone number and business name. I like the idea of a shield shape with a banner since it would more eye catching, Once again the Stonebrook image and name is less important than communicating what the business does. I like Crimson, grey, gold, black but am open to new ideas . I like the idea of a shield with a banner more than a rectangle, but am open to idea's

Target Market(s)

My target market is local homeowners ($700k+) who want a relationship with their framer and are willing to pay for a customized experience compared to a craft store experience. I have more female clients then men.

Industry/Entity Type

Picture Framing Art

Other font styles liked:
• Look at the attached image of a custom pizzeria sign, its kid of a custom car pinstripe font style. Script and decorative may be difficult to read while driving by but add to the elegance.

Colors

Designer to choose colors to be used in the design.

Requirements
Must have
• Clearly communicate what the business does "Custom framing" preferably with a picture frame and words
Nice to have
• incorporate a Stonebrook into the graphic
Should not have
• A Stonebrook image doesn't communicate what the business does to a vehicle traveling at 40 mph by the sign

```html
<!DOCTYPE html>
<html lang="en">
<head>
<meta charset="utf-8">
<title>Stonebrook Framing Studio – Custom Framing Sign</title>
<link rel="stylesheet" href="https://fonts.googleapis.com/css2?family=Vollkorn:wght@600;700;800&family=Cormorant+Garamond:wght@500;600&display=swap">
<style>
  :root {
    --crimson: #7f2a2f;
    --crimson-dark: #5e1c21;
    --cream: #ebd0a8;
    --gold: #c99a5b;
    --gold-light: #dcb37a;
    --black: #16161b;
    --ink: #1e1a1a;
    --page: #ffffff;
  }
  html, body {
    margin: 0;
    padding: 0;
    width: 1200px;
    height: 720px;
    overflow: hidden;
    background: var(--page);
  }
  .canvas {
    position: relative;
    width: 1200px;
    height: 720px;
  }
  .sign {
    position: absolute;
    left: 330px;
    top: 38px;
    width: 541px;
    height: 644px;
  }
  .shield-outer { fill: var(--black); }
  .shield-gold { fill: var(--gold); }
  .shield-rim { fill: var(--cream); }
  .shield-field { fill: var(--cream); }
  .shield-pinline { fill: none; stroke: var(--crimson); stroke-width: 2; }
  .shield-goldline { fill: none; stroke: var(--gold); stroke-width: 6; }

  .divider-line { stroke: var(--gold); stroke-width: 4; stroke-linecap: round; }
  .ornament { fill: var(--gold); }
  .emblem { fill: var(--crimson); }

  .headline {
    font-family: "Vollkorn", Georgia, serif;
    font-weight: 700;
    font-size: 150px;
    fill: var(--crimson);
    stroke: var(--gold-light);
    stroke-width: 5;
    paint-order: stroke fill;
  }
  .headline-shadow {
    font-family: "Vollkorn", Georgia, serif;
    font-weight: 700;
    font-size: 150px;
    fill: var(--gold);
  }
  .appointment {
    font-family: "Cormorant Garamond", Georgia, serif;
    font-weight: 600;
    font-size: 40px;
    fill: var(--ink);
  }
  .studio-name {
    font-family: "Vollkorn", Georgia, serif;
    font-weight: 700;
    font-size: 84px;
    fill: var(--crimson);
  }
  .studio-tag {
    font-family: "Vollkorn", Georgia, serif;
    font-weight: 700;
    font-size: 21px;
    fill: var(--crimson);
  }
  .banner-band { fill: var(--crimson); stroke: var(--gold); stroke-width: 4; }
  .banner-tail { fill: var(--crimson-dark); stroke: var(--gold); stroke-width: 4; }
  .banner-fold { fill: #3f1216; }
  .phone {
    font-family: "Vollkorn", Georgia, serif;
    font-weight: 700;
    font-size: 74px;
    fill: var(--cream);
  }
</style>
</head>
<body>
<main class="canvas">
  <svg class="sign" viewBox="195 205 940 1120" xmlns="http://www.w3.org/2000/svg" aria-label="Custom Framing by appointment, Stonebrook Framing Studio, (555) 014 2290">
    <defs>
      <path id="shield" d="M 668 212 C 520 212 440 250 390 300 L 282 300 C 280 340 260 365 208 368 L 208 820 C 230 1080 480 1230 668 1302 C 856 1230 1106 1080 1128 820 L 1128 368 C 1076 365 1056 340 1054 300 L 945 300 C 895 250 816 212 668 212 Z"/>
      <path id="phone-arc" d="M 380 1150 Q 668 1240 960 1110"/>
    </defs>

    <!-- shield body -->
    <use href="#shield" class="shield-outer"/>
    <use href="#shield" class="shield-gold" transform="translate(668 760) scale(0.962) translate(-668 -760)"/>
    <use href="#shield" class="shield-rim" transform="translate(668 760) scale(0.945) translate(-668 -760)"/>
    <use href="#shield" class="shield-goldline" transform="translate(668 760) scale(0.93) translate(-668 -760)"/>
    <use href="#shield" class="shield-field" transform="translate(668 760) scale(0.915) translate(-668 -760)"/>
    <use href="#shield" class="shield-pinline" transform="translate(668 760) scale(0.89) translate(-668 -760)"/>

    <!-- top emblem and divider -->
    <ellipse class="emblem" role="img" aria-label="Hawk with spread wings illustration" cx="665" cy="360" rx="72" ry="42"/>
    <line class="divider-line" x1="450" y1="401" x2="600" y2="401"/>
    <line class="divider-line" x1="735" y1="401" x2="880" y2="401"/>
    <ellipse class="ornament" role="img" aria-label="Gold flourish" cx="412" cy="401" rx="30" ry="14"/>
    <ellipse class="ornament" role="img" aria-label="Gold flourish" cx="918" cy="401" rx="30" ry="14"/>

    <!-- headline -->
    <text class="headline-shadow" x="664" y="590" text-anchor="middle" textLength="640" lengthAdjust="spacingAndGlyphs">CUSTOM</text>
    <text class="headline" x="658" y="583" text-anchor="middle" textLength="640" lengthAdjust="spacingAndGlyphs">CUSTOM</text>
    <text class="headline-shadow" x="672" y="740" text-anchor="middle" textLength="750" lengthAdjust="spacingAndGlyphs">FRAMING</text>
    <text class="headline" x="666" y="733" text-anchor="middle" textLength="750" lengthAdjust="spacingAndGlyphs">FRAMING</text>

    <!-- appointment line -->
    <ellipse class="ornament" role="img" aria-label="Gold flourish" cx="410" cy="806" rx="22" ry="13"/>
    <ellipse class="ornament" role="img" aria-label="Gold flourish" cx="924" cy="806" rx="22" ry="13"/>
    <text class="appointment" x="667" y="820" text-anchor="middle" textLength="405" lengthAdjust="spacing">BY APPOINTMENT</text>
    <line class="divider-line" x1="412" y1="856" x2="918" y2="856"/>
    <ellipse class="ornament" role="img" aria-label="Gold centre scroll" cx="665" cy="860" rx="40" ry="14"/>

    <!-- studio name -->
    <text class="studio-name" x="668" y="1010" text-anchor="middle" textLength="440" lengthAdjust="spacingAndGlyphs">Stonebrook</text>
    <text class="studio-tag" x="730" y="1066" text-anchor="middle">FRAMING STUDIO</text>

    <!-- banner -->
    <path class="banner-tail" d="M 262 1000 L 365 1048 L 350 1168 L 225 1108 L 300 1085 Z"/>
    <path class="banner-tail" d="M 1072 1000 L 968 1045 L 985 1160 L 1110 1108 L 1035 1082 Z"/>
    <path class="banner-fold" d="M 340 1052 L 365 1048 L 350 1168 L 318 1160 Z"/>
    <path class="banner-fold" d="M 968 1045 L 995 1040 L 1012 1155 L 985 1160 Z"/>
    <path class="banner-band" d="M 338 1055 Q 668 1150 972 1040 L 1010 1150 Q 668 1295 320 1165 Z"/>
    <text class="phone" text-anchor="middle"><textPath href="#phone-arc" startOffset="50%">(555) 014 2290</textPath></text>
  </svg>
</main>
</body>
</html>
```